Heritage Hollow Business Cards

Require a business card design. <br/><br/>Needs to include logo (either round or long version) plus these details:<br/>Maya Torvel<br/>Heritage Hollow<br/>maya@quonbrook.com.au<br/>02 6481 7390<br/>PO Box Glenwarra NSW 2913<br/>www.heritagehollow.com.au<br/><br/>I need in an editable format so that I can create for multiple staff members. <br/><br/>

Target Market(s)

We are an online store selling renovation products to home owners are builders. Looking for a classic classy design.

Industry/Entity Type

Home And Garden

Contact Information for Business Card

Maya Torvel
Heritage Hollow
maya@quonbrook.com.au
02 6481 7390
PO Box Glenwarra NSW 2913
www.heritagehollow.com.au

Colors

Designer to choose colors to be used in the design.

Requirements
Must have
• Must include Logo.

```html
<!DOCTYPE html>
<html lang="en">
<head>
<meta charset="utf-8">
<title>Heritage Hollow – Business Cards</title>
<link href="https://fonts.googleapis.com/css2?family=Questrial&family=Source+Sans+3:wght@400;600&display=swap" rel="stylesheet">
<style>
  :root {
    --backdrop: #c1c1c1;
    --card-light: #f8f8f8;
    --panel-white: #ffffff;
    --ink-black: #121317;
    --ink-charcoal: #262626;
    --sage: #526f61;
    --text-light: #ffffff;
    --text-dark: #1b1b1b;
  }
  * { box-sizing: border-box; margin: 0; padding: 0; }
  html, body {
    width: 927px; height: 1200px; overflow: hidden;
    background: var(--backdrop);
  }
  .sheet { position: relative; width: 927px; height: 1200px; }

  .card {
    position: absolute; left: 132px; width: 688px; height: 396px;
    background: var(--card-light); overflow: hidden;
  }
  .card-shadow {
    position: absolute; left: 150px; width: 652px; height: 26px;
    border-radius: 50%;
    background: rgba(0,0,0,0.28);
    filter: blur(12px);
  }
  .card--front { top: 134px; }
  .card-shadow--front { top: 522px; }
  .card--back { top: 612px; height: 398px; }
  .card-shadow--back { top: 1000px; }

  /* Front */
  .front-dark {
    position: absolute; left: 241px; top: 0; right: 0; bottom: 0;
    background: var(--ink-black);
  }
  .front-strip {
    position: absolute; left: 216px; top: 0; width: 49px; height: 396px;
    border-radius: 25px; background: var(--sage);
  }
  .brand-seal {
    position: absolute; left: 33px; top: 108px; width: 164px; height: 164px;
    border: 1px solid var(--text-dark); border-radius: 50%;
    display: flex; align-items: center; justify-content: center;
    font-family: "Source Sans 3", sans-serif; font-weight: 600;
    font-size: 24px; line-height: 1.05; color: var(--text-dark);
    text-align: left;
  }
  .holder-name {
    position: absolute; left: 311px; top: 30px; width: 360px;
    font-family: "Questrial", sans-serif; font-weight: 400; font-size: 48px; line-height: 1;
    letter-spacing: 1px; color: var(--text-light); white-space: nowrap;
  }
  .holder-role {
    position: absolute; left: 311px; top: 86px;
    font-family: "Questrial", sans-serif; font-size: 26px; line-height: 1;
    color: var(--text-light);
  }
  .contact-list { list-style: none; }
  .contact-item {
    position: absolute; left: 277px;
    font-family: "Source Sans 3", sans-serif; font-size: 26px; line-height: 1;
    color: var(--text-light); white-space: nowrap;
  }
  .contact-item--phone { top: 166px; }
  .contact-item--email { top: 217px; }
  .contact-item--web { top: 270px; }
  .contact-item--post { top: 324px; font-size: 23px; left: 276px; }
  .contact-icon {
    position: absolute; left: -52px; width: 30px; height: 30px;
    fill: var(--text-light);
  }

  /* Back */
  .back-panel {
    position: absolute; left: 72px; top: 70px; width: 557px; height: 194px;
    background: var(--panel-white);
    display: flex; align-items: center; justify-content: center;
  }
  .back-wordmark {
    font-family: "Source Sans 3", sans-serif; font-weight: 600;
    font-size: 58px; color: var(--text-dark); line-height: 1;
  }
  .back-arc {
    position: absolute; left: 1px; right: 1px; top: 281px; height: 60px;
    background: var(--sage); border-radius: 45px 45px 0 0;
  }
  .back-footer {
    position: absolute; left: 1px; right: 1px; top: 326px; bottom: 0;
    background: var(--ink-charcoal);
    display: flex; align-items: center; justify-content: center;
    font-family: "Source Sans 3", sans-serif; font-size: 17px;
    color: var(--text-light); letter-spacing: 0.3px;
  }
</style>
</head>
<body>
<main class="sheet">
  <div class="card-shadow card-shadow--front"></div>
  <section class="card card--front" aria-label="Business card front">
    <div class="front-dark"></div>
    <div class="front-strip"></div>
    <div class="brand-seal">Heritage<br>Hollow</div>
    <h1 class="holder-name">MAYA TORVEL</h1>
    <p class="holder-role">Director</p>
    <ul class="contact-list">
      <li class="contact-item contact-item--phone">
        <svg class="contact-icon" style="top:-2px" viewBox="0 0 24 24" aria-hidden="true"><path d="M6.6 2.5c.6-.4 1.4-.2 1.8.4l2 3.3c.4.6.2 1.4-.3 1.8l-1.4 1c.9 2.2 2.6 4 4.8 5l1-1.4c.4-.6 1.2-.8 1.8-.4l3.3 2c.6.4.8 1.2.4 1.8l-1.2 2c-.6 1-1.8 1.5-3 1.2C9.6 17.6 5.900 13.9 4.3 7.9c-.3-1.2.2-2.4 1.2-3z"/></svg>
        02 6481 7390
      </li>
      <li class="contact-item contact-item--email">
        <svg class="contact-icon" style="top:-4px" viewBox="0 0 24 24" aria-hidden="true"><path d="M2 5h20v14H2zM3.6 6.3v.2L12 12.8l8.4-6.3v-.2zm0 1.9v9.5l5.6-5.3zm16.8 0-5.6 4.2 5.6 5.3zM10 13l-6.1 5.7h16.2L14 13l-2 1.5z"/></svg>
        maya@quonbrook.com.au
      </li>
      <li class="contact-item contact-item--web">
        <svg class="contact-icon" style="top:-4px" viewBox="0 0 24 24" aria-hidden="true"><path d="M12 1.5a10.5 10.5 0 1 0 0 21 10.5 10.5 0 0 0 0-21zm0 2a8.5 8.5 0 0 1 7.4 4.3h-3.2l-1.4 1.8-2.4-.6-1.3 2 1.6 2.2h2.5l.8 3.2-1.7 3.6A8.5 8.5 0 0 1 4 14.5l2.3-.4 1.5 1.8.6 3.1 1.3-.1-.2-3.300 1.5-2-2.4-2.6H6.1L4 9.2A8.5 8.5 0 0 1 12 3.5z"/></svg>
        www.heritagehollow.com.au
      </li>
      <li class="contact-item contact-item--post">
        <svg class="contact-icon" style="top:-9px;left:-51px;height:34px" viewBox="0 0 24 24" aria-hidden="true"><path d="M12 1a7.5 7.5 0 0 0-7.5 7.5C4.5 14 12 23 12 23s7.5-9 7.5-14.5A7.5 7.5 0 0 0 12 1zm0 4.2a3.3 3.3 0 1 1 0 6.6 3.3 3.3 0 0 1 0-6.6z"/></svg>
        PO Box Glenwarra NSW 2913
      </li>
    </ul>
  </section>

  <div class="card-shadow card-shadow--back"></div>
  <section class="card card--back" aria-label="Business card back">
    <div class="back-panel">
      <span class="back-wordmark">Heritage Hollow</span>
    </div>
    <div class="back-arc"></div>
    <div class="back-footer">www.heritagehollow.com.au</div>
  </section>
</main>
</body>
</html>
```